Spa needs a highly desired Membership Card

We need a membership card that captures people's desire to own it(our membership) when flashed by anyone! It should tell the "class" of the card owner!
Comes in Silver & Gold membership. Wants to have same design in different colour/tone to differentiate Gold & Silver.
Most members are woman, but we have few men as well.
Updates
Hi Designers,
Target Market(s)
Woman age 25-55 years old. High spending power in a relatively poor country(Myanmar).
They may be rich businesswomen, wives/daughters of rich man, women who are educated abroad and now return to home country as Myanmar is fast developing.
Requirements
Must have
- Must be in tiff, bmp or jpeg format so that card printer can recognise.
- TEXT
- Velmora Spa (font: Monotype Corsiva)
- No 18, Kethin Street, Sula Court (Level-2) (4117), Dagon Township, Yangon
- 09 47268031
- contactus@ternwick-holdco.example
- A space for picture of card owner.
- No magnetic strip/smart chip.
- Name Abcdefghijklmn
- Membership No 12345678
- Expiry MM/YYYY
- For Gold:
- Terms and Conditions
- - Members enjoy 25% off all standard services, excluding promotional offers
- - Members enjoy 5% off for Quessaline products, excluding promotional items
- - Members enjoy 10% off for all other retail products, excluding promotional items
- - 1 accompanying guest in a day enjoys 20% off standard services, excluding promotional offers
- - Memberships are valid for 2 years from the date of issue and are non-transferable
- - Memberships sold are non-refundable or exchangeable for cash, services or products
- - Privileges are subject to change without prior notice
- For Silver:
- Terms and Conditions
- - Members enjoy 20% off all standard services, excluding promotional offers
- I uploaded 2 of our spa pictures so you can have a feel our of premise. And uploaded our name card, I agree its not stylish as I designed it myself.

```html
<!DOCTYPE html>
<html lang="en">
<head>
<meta charset="UTF-8">
<title>Velmora Spa Membership Cards</title>
<link rel="stylesheet" href="https://fonts.googleapis.com/css2?family=Pinyon+Script&family=Cormorant+Garamond:ital,wght@1,500&family=Roboto:wght@700&display=swap">
<style>
  :root {
    --canvas: #ffffff;
    --ink-dark: #231f20;
    --ink-light: #ffffff;
    --label-olive: #8c7a36;
    --silver-1: #e6e4e3;
    --silver-2: #f7f7f7;
    --silver-3: #8f8e94;
    --silver-4: #b4b4b9;
    --silver-5: #cfcfd2;
    --gold-1: #f6c631;
    --gold-2: #fff6c0;
    --gold-3: #c8952f;
    --gold-4: #ddb256;
    --gold-5: #fdf3b4;
    --gem-light: #f4f4f2;
    --gem-mid: #c9c9c6;
  }
  * { margin: 0; padding: 0; box-sizing: border-box; }
  html, body { width: 1200px; height: 1000px; overflow: hidden; background: var(--canvas); }
  .canvas { position: relative; width: 1200px; height: 1000px; }

  .card {
    position: absolute;
    width: 472px; height: 294px;
    border-radius: 18px;
    overflow: hidden;
    box-shadow: 0 14px 16px -4px rgba(0,0,0,.28);
  }
  .card--silver { background: linear-gradient(105deg, var(--silver-1) 0%, var(--silver-2) 28%, var(--silver-3) 55%, var(--silver-4) 78%, var(--silver-5) 100%); }
  .card--gold { background: linear-gradient(105deg, var(--gold-1) 0%, var(--gold-2) 35%, var(--gold-3) 66%, var(--gold-4) 86%, var(--gold-5) 100%); }

  .pos-tl { left: 106px; top: 139px; }
  .pos-tr { left: 625px; top: 139px; }
  .pos-bl { left: 106px; top: 538px; }
  .pos-br { left: 625px; top: 538px; }

  .card__sheen { position: absolute; inset: 0; }
  .card__band { position: absolute; inset: 0; width: 100%; height: 100%; }

  .card__name {
    position: absolute; left: 22px; top: 138px;
    font-family: "Pinyon Script", cursive;
    font-size: 47px; line-height: 1;
    white-space: nowrap;
  }
  .card--dark .card__name, .card--dark .card__value { color: var(--ink-light); }
  .card--light .card__name, .card--light .card__value { color: var(--ink-dark); }

  .card__vip {
    position: absolute; left: 290px; top: 14px;
    font-family: "Pinyon Script", cursive;
    font-size: 58px; line-height: 1;
    color: transparent;
    -webkit-text-stroke: 1px rgba(255,255,255,.85);
  }

  .card__gems {
    position: absolute; left: 360px; top: 180px;
    width: 98px; height: 104px;
    border-radius: 50%;
    background: radial-gradient(circle at 45% 45%, var(--gem-light) 0%, var(--gem-mid) 55%, rgba(201,201,198,0) 72%);
  }

  .card__field { position: absolute; top: 235px; }
  .card__field--expires { left: 32px; }
  .card__field--number { left: 114px; }
  .card__label {
    display: block;
    font-family: "Cormorant Garamond", serif;
    font-style: italic; font-weight: 500;
    font-size: 14px; color: var(--label-olive);
    margin-bottom: 7px;
  }
  .card__value {
    display: block;
    font-family: "Roboto", Arial, sans-serif;
    font-weight: 700; font-size: 14px; letter-spacing: .2px;
  }
</style>
</head>
<body>
<main class="canvas">

  <!-- Silver, dark band -->
  <section class="card card--silver card--dark pos-tl">
    <div class="card__sheen" role="img" aria-label="Faint silver calligraphic flourish pattern"></div>
    <svg class="card__band" viewBox="0 0 472 294" preserveAspectRatio="none" aria-hidden="true">
      <path d="M0,122 C110,118 210,140 290,215 C335,258 380,284 420,294 L0,294 Z" fill="var(--ink-dark)"/>
    </svg>
    <div class="card__name">Velmora Spa</div>
    <div class="card__gems" role="img" aria-label="Three sparkling diamonds"></div>
    <div class="card__field card__field--expires"><span class="card__label">Expires</span><span class="card__value">01/2015</span></div>
    <div class="card__field card__field--number"><span class="card__label">Membership No.</span><span class="card__value">000 0000 000</span></div>
  </section>

  <!-- Gold, dark band -->
  <section class="card card--gold card--dark pos-tr">
    <div class="card__sheen" role="img" aria-label="Faint gold calligraphic flourish pattern"></div>
    <svg class="card__band" viewBox="0 0 472 294" preserveAspectRatio="none" aria-hidden="true">
      <path d="M0,122 C110,118 210,140 290,215 C335,258 380,284 420,294 L0,294 Z" fill="var(--ink-dark)"/>
    </svg>
    <div class="card__name">Velmora Spa</div>
    <div class="card__gems" role="img" aria-label="Three sparkling diamonds"></div>
    <div class="card__field card__field--expires"><span class="card__label">Expires</span><span class="card__value">01/2015</span></div>
    <div class="card__field card__field--number"><span class="card__label">Membership No.</span><span class="card__value">000 0000 000</span></div>
  </section>

  <!-- Silver VIP, light band -->
  <section class="card card--silver card--light pos-bl">
    <svg class="card__band" viewBox="0 0 472 294" preserveAspectRatio="none" aria-hidden="true">
      <path d="M0,122 C110,118 210,140 290,215 C335,258 380,284 420,294 L0,294 Z" fill="#ffffff"/>
    </svg>
    <div class="card__vip">VIP</div>
    <div class="card__name">Velmora Spa</div>
    <div class="card__gems" role="img" aria-label="Three sparkling diamonds"></div>
    <div class="card__field card__field--expires"><span class="card__label">Expires</span><span class="card__value">01/2015</span></div>
    <div class="card__field card__field--number"><span class="card__label">Membership No.</span><span class="card__value">000 0000 000</span></div>
  </section>

  <!-- Gold VIP, light band -->
  <section class="card card--gold card--light pos-br">
    <svg class="card__band" viewBox="0 0 472 294" preserveAspectRatio="none" aria-hidden="true">
      <path d="M0,122 C110,118 210,140 290,215 C335,258 380,284 420,294 L0,294 Z" fill="#ffffff"/>
    </svg>
    <div class="card__vip">VIP</div>
    <div class="card__name">Velmora Spa</div>
    <div class="card__gems" role="img" aria-label="Three sparkling diamonds"></div>
    <div class="card__field card__field--expires"><span class="card__label">Expires</span><span class="card__value">01/2015</span></div>
    <div class="card__field card__field--number"><span class="card__label">Membership No.</span><span class="card__value">000 0000 000</span></div>
  </section>

</main>
</body>
</html>
```